依頼詳細
カキ氷店を新規オープンする企業です。
当社商品の特徴をわかりやすく、魅力的に表現にして頂きたく募集致しました。
誰もが理解できるわかりやすいデザインのご提案をお願い致します。

1、チャレンジかき氷(手動のカキ氷機でお客様自身にカキ氷を製造して頂きます。)
・カキ氷専用の氷を使用します。(通常なら48時間で「純氷」となるところを、さらに長い72時間かけてじっくりと凍らせたかき氷専用の氷)

2、ふわとろカキ氷(台湾カキ氷)
(こちらの商品は製造してご提供致します。)
・フルーツ含有量90%の高級果実ピューレと共にお召し上がり頂きます。
記載項目
看板(横断幕)の記載内容は下記になります。
■看板(横断幕)サイズ、縦1200mm:横3000mm(多少の変更あり)
■店名、汐凪カキ氷本舗
■依頼詳細の1、2の内容
■カキ氷の画像
・チャレンジかき氷はカキ氷機の画像(添付画像①あり)
・ふわとろカキ氷(台湾カキ氷)の画像(参考添付画像②あり)
・上記2点の画像はサイズの大きいタイプの用意ができませんので、CG、イラストで問題ございません。

※店前に添付画像③のような立て看板(幕)も設置致しますので、上記と同様の内容でご提案頂けますようお願い致します。
■看板(幕)サイズ、縦2000mm:横1200mm(多少の変更あり)
希望イメージ
シンプル 複雑
単色 カラフル
暗い 明るい
日常 高級
遊び心 厳粛
未来的 伝統的
女性的 男性的
希望する色
青系、水色系
納品ファイル
• 高解像度JPG (.jpg)
• イラストレーター形式 (.ai)
補足説明
納品データは、aiでお願い致します。
納品以前のご提案は、Jpgでお願い致します。
デザインを依頼している看板(横断幕)のサイズが決定致しました。
サイズ:縦1800mm:横4000mmで決定致しましたのでご提案お願い致します。

同様に立て看板(幕)のサイズも縦2000mm:横1200mmで決定致しましたのでご提案お願い致します。

立て看板のデザインに関しては、横断幕と内容が同じであれば、違うデザインでもOKです。
古風・和・高級感・シンプルをイメージするようなデザインをご提案して頂く事は可能でしょうか?

使用する横断幕は、下記URLのショップで発注予定です。
http://www.kelsaro.net/html/service/ou1.html
ふわとろカキ氷の商品イメージ画像を新たに添付致しますのでご確認下さい。
商品画像イメージ1’・2’をアップ致しました。
募集を延期致しました。
カキ氷の追加画像です。
今回アップしたサイズが最大の画像になります。

当社の依頼内容が最も反映されたデザインだったから。
また追記の内容にも即座に反応して頂けたから。
当選のクリフォ様のご対応が迅速且つ大変丁寧だったから。
最終的に好みだったから。

この度は、当社の看板デザイン募集にたくさんご応募頂き、誠にありがとうございました。
また看板デザインという大変な作業にも関わらず、本当にご応募頂きありがとうございました。
またクリフォンでお仕事を依頼させて頂きますので今後とも宜しくお願い致します。
この度は、誠にありがとうございました。

```html
<!DOCTYPE html>
<html lang="ja">
<head>
<meta charset="utf-8">
<title>汐凪カキ氷本舗 立て看板</title>
<link href="https://fonts.googleapis.com/css2?family=Shippori+Mincho+B1:wght@700;800&family=Yuji+Boku&display=swap" rel="stylesheet">
<style>
  :root {
    --frame-brown: #6b4a2a;
    --paper: #f4e7c4;
    --paper-deep: #e6d3a2;
    --ink: #2b1d12;
    --red: #d9231c;
    --red-dark: #b3150f;
    --label-cream: #fbf4e2;
    --white: #ffffff;
    --ice-pink: #e87a78;
    --machine-teal: #52b3bf;
  }
  html, body { margin: 0; padding: 0; overflow: hidden; background: #fff; }
  .signboard {
    position: relative;
    width: 721px; height: 1200px;
    box-sizing: border-box;
    border: 7px solid var(--frame-brown);
    background: radial-gradient(ellipse at 50% 45%, var(--paper) 55%, var(--paper-deep) 100%);
    overflow: hidden;
    font-family: "Shippori Mincho B1", serif;
    color: var(--ink);
  }
  .signboard::after {
    content: ""; position: absolute; inset: 10px;
    border: 2px solid rgba(107,74,42,.35);
    pointer-events: none;
  }
  .vertical { writing-mode: vertical-rl; position: absolute; font-weight: 800; line-height: 1.15; }
  .tcy { text-combine-upright: all; }

  .menu-label {
    position: absolute;
    background: var(--label-cream);
    border: 2px solid var(--ink);
    box-shadow: 3px 4px 0 rgba(60,40,20,.25);
  }
  .menu-label__cap {
    position: absolute; left: -8px; right: -8px; top: -18px; height: 40px;
    background: var(--red); border: 2px solid var(--red-dark);
  }
  .menu-label__text {
    writing-mode: vertical-rl; position: absolute; top: 42px;
    font-weight: 800; line-height: 1.2; color: var(--ink);
  }
  .menu-label--challenge { left: 118px; top: 128px; width: 78px; height: 250px; }
  .menu-label--challenge .menu-label__text { right: 6px; font-size: 33px; }
  .menu-label--fuwatoro { left: 515px; top: 370px; width: 86px; height: 330px; }
  .menu-label--fuwatoro .menu-label__text { right: 8px; font-size: 31px; }
  .menu-label__sub { font-size: 25px; }

  .shaved-ice-photo {
    position: absolute; left: 493px; top: 48px; width: 190px; height: 228px;
    border-radius: 48% 52% 20% 20%;
    background: radial-gradient(circle at 45% 40%, #f3a19b, var(--ice-pink) 60%, #c9d6dc 95%);
  }
  .ice-machine-illustration {
    position: absolute; left: 26px; top: 820px; width: 286px; height: 356px;
    border-radius: 18px;
    background: linear-gradient(160deg, #7fcbd4, var(--machine-teal) 60%, #3a8d98);
  }

  .shop-name-region {
    position: absolute; left: 268px; top: 196px; width: 140px; height: 74px;
    background: var(--white); border-radius: 40px;
    display: flex; align-items: center; justify-content: center;
    color: var(--red); font-size: 52px; font-weight: 800; letter-spacing: 4px;
    z-index: 2;
  }
  .title-banner { position: absolute; left: 262px; top: 250px; width: 246px; height: 770px; }
  .title-banner svg { position: absolute; inset: 0; }
  .title-banner__text {
    writing-mode: vertical-rl; position: absolute; left: 0; right: 0; top: 60px;
    margin: 0 auto; text-align: center;
    font-family: "Yuji Boku", serif; font-size: 128px; line-height: 1;
    color: var(--white); letter-spacing: 6px;
    text-shadow: 3px 3px 0 var(--red-dark);
  }

  .challenge-copy { left: 148px; top: 398px; font-size: 33px; }
  .fruit-copy { left: 548px; top: 728px; font-size: 36px; }
</style>
</head>
<body>
<main class="signboard">
  <div class="shaved-ice-photo" role="img" aria-label="台湾風ふわとろカキ氷（苺ピューレがけ）の写真"></div>

  <div class="menu-label menu-label--challenge">
    <div class="menu-label__cap"></div>
    <div class="menu-label__text">チャレンジ<br>カキ氷</div>
  </div>

  <p class="vertical challenge-copy" style="margin:0">手動のカキ氷機で<br>自分で作成！</p>

  <div class="shop-name-region">汐凪</div>
  <div class="title-banner">
    <svg viewBox="0 0 246 770" preserveAspectRatio="none" aria-hidden="true">
      <path fill="var(--red)" d="M10 4 L60 12 L120 2 L180 10 L240 4 L232 80 L244 160 L234 260 L242 360 L232 460 L244 560 L234 660 L240 766 L180 758 L120 768 L60 760 L6 766 L14 660 L2 560 L12 460 L4 360 L14 260 L2 160 L12 80 Z"/>
    </svg>
    <h1 class="title-banner__text" style="margin-left:auto;margin-right:auto">カキ氷本舗</h1>
  </div>

  <div class="menu-label menu-label--fuwatoro">
    <div class="menu-label__cap"></div>
    <div class="menu-label__text">ふわとろカキ氷<br><span class="menu-label__sub">（台湾カキ氷）</span></div>
  </div>

  <p class="vertical fruit-copy" style="margin:0">フルーツ含有量<span class="tcy">90</span>%<br>高級果実ピューレ</p>

  <div class="ice-machine-illustration" role="img" aria-label="手回し式の水色のカキ氷機のイラスト"></div>
</main>
</body>
</html>
```